Dental Business Card Design w/logo

Classic, elegant w/a touch of contemporary
Upscale dental facility located in Modesto CA
Specializing in restorative & general dentistry
Providing exceptional customer service to the community
Updates

I prefer script and not bold writing
If you can use the phone; fax and email icons instead of spelling them out, it would be great
No bold colors
Classy and elegant
In the back of the card I would like to see something like this
Your Next Appointment:
Mon     Tue    Wed    Thur (a box next to each of them for marking)
Date:_______________ at_____________ AM    PM  (a box next to them for marking)

Thank you

Target Market(s)

Well established professional

Industry/Entity Type

Dental

Contact Information for Business Card

Velorine Tamsuki DMD
4176 Larchmont Rd
Suite D7
Modesto, CA 95368

Office: 209-731-5092
Fax: 209-731-8247
Email: tamsukidmd@brivelmail.test

Requirements
Must have
• Unique classic logo
An easily repeatable design that can be used on letterhead and envelopes
Nice to have
• My initials incorporated into unique design
Should not have
• No cartoons or cheesy themes. This is a practice for the well established and professional individual.

```html
<!DOCTYPE html>
<html lang="en">
<head>
<meta charset="utf-8">
<title>Velorine Tamsuki DMD – Business Card</title>
<link rel="stylesheet" href="https://fonts.googleapis.com/css2?family=Great+Vibes&display=swap">
<style>
  :root {
    --page-bg: #eef0f1;
    --card-white: #ffffff;
    --card-grey: #e1e2e4;
    --card-edge: #3a3a3a;
    --ink: #1b1b1b;
    --accent-blue: #1e93d8;
    --box-white: #ffffff;
  }
  html, body {
    margin: 0;
    padding: 0;
    width: 1200px;
    height: 1200px;
    overflow: hidden;
    background: var(--page-bg);
    font-family: "Great Vibes", cursive;
    color: var(--ink);
  }
  .canvas {
    position: relative;
    width: 1200px;
    height: 1200px;
  }
  .card {
    position: absolute;
    left: 228px;
    width: 742px;
    height: 422px;
    border: 1.5px solid var(--card-edge);
    box-sizing: border-box;
    overflow: hidden;
  }
  .card-front {
    top: 168px;
    background: linear-gradient(90deg, #dcdde0 0%, var(--card-white) 14%, var(--card-white) 100%);
    border-radius: 0 38px 0 38px;
  }
  .card-back {
    top: 612px;
    background: radial-gradient(ellipse at 45% 40%, #f6f6f7 0%, var(--card-grey) 70%);
    border-radius: 38px 0 38px 0;
  }
  .brand {
    position: absolute;
    display: flex;
    align-items: center;
    gap: 14px;
  }
  .brand-dot {
    width: 46px;
    height: 46px;
    border-radius: 50%;
    background: var(--accent-blue);
    flex: none;
  }
  .brand-name {
    font-size: 34px;
    line-height: 32px;
    color: var(--ink);
    margin: 0;
    font-weight: 400;
  }
  .card-front .brand { left: 510px; top: 46px; }
  .card-back .brand { left: 84px; top: 46px; }

  .contact-list {
    position: absolute;
    left: 52px;
    top: 264px;
    margin: 0;
    padding: 0;
    list-style: none;
    font-size: 16px;
    line-height: 20px;
  }
  .contact-item {
    display: flex;
    align-items: flex-start;
    gap: 10px;
    margin-bottom: 3px;
  }
  .contact-icon {
    width: 18px;
    height: 18px;
    flex: none;
    fill: var(--accent-blue);
  }
  .contact-item.email { margin-top: 6px; font-size: 14px; }

  .appointment {
    position: absolute;
    left: 370px;
    top: 276px;
    width: 340px;
  }
  .appointment-title {
    margin: 0 0 4px;
    font-size: 19px;
    font-weight: 400;
    color: var(--accent-blue);
  }
  .appointment-row {
    margin-left: 50px;
    display: flex;
    align-items: center;
    gap: 3px;
    font-size: 17px;
    line-height: 26px;
    white-space: nowrap;
  }
  .check-box {
    display: inline-block;
    width: 14px;
    height: 12px;
    background: var(--box-white);
    margin-right: 10px;
  }
  .check-box:last-child { margin-right: 0; }
  .fill-line {
    display: inline-block;
    border-bottom: 1px solid var(--ink);
    height: 16px;
  }
  .fill-line.date { width: 66px; }
  .fill-line.time { width: 44px; }
</style>
</head>
<body>
<main class="canvas">

  <section class="card card-front" aria-label="Card front">
    <div class="brand">
      <span class="brand-dot" aria-hidden="true"></span>
      <h1 class="brand-name">Velorine<br>Tamsuki<br>DMD</h1>
    </div>

    <ul class="contact-list">
      <li class="contact-item address">
        <svg class="contact-icon" viewBox="0 0 18 18" aria-label="Address"><path d="M9 2 1 9h2.5v7h4v-5h3v5h4V9H17z"/></svg>
        <span>4176 Larchmont Rd Suite D7 Modesto,<br>CA 95368</span>
      </li>
      <li class="contact-item phone">
        <svg class="contact-icon" viewBox="0 0 18 18" aria-label="Office"><path d="M4.5 2 7 5.5 5.6 7.3c.9 2 2.5 3.6 4.6 4.7l1.8-1.4L16 13l-1.2 2.8C9 16 2 9.3 2.2 3.3z"/></svg>
        <span>209-731-5092</span>
      </li>
      <li class="contact-item fax">
        <svg class="contact-icon" viewBox="0 0 18 18" aria-label="Fax"><path d="M5 2h8v4H5z"/><path d="M2 7h14v8H2zm3 2v2h2V9zm4 0v2h4V9zm-4 3v1h8v-1z" fill-rule="evenodd"/></svg>
        <span>209-731-8247</span>
      </li>
      <li class="contact-item email">
        <svg class="contact-icon" viewBox="0 0 18 18" aria-label="Email"><path d="M2 4h14v10H2z"/><path d="M2 4l7 6 7-6" fill="none" stroke="#fff" stroke-width="1.4"/></svg>
        <span>tamsukidmd@brivelmail.test</span>
      </li>
    </ul>
  </section>

  <section class="card card-back" aria-label="Card back">
    <div class="brand">
      <span class="brand-dot" aria-hidden="true"></span>
      <p class="brand-name">Velorine<br>Tamsuki<br>DMD</p>
    </div>

    <div class="appointment">
      <h2 class="appointment-title">Next Appointment:</h2>
      <div class="appointment-row">
        <span>Mon</span><span class="check-box"></span>
        <span>Tue</span><span class="check-box"></span>
        <span>Wed</span><span class="check-box"></span>
        <span>Thur</span><span class="check-box"></span>
      </div>
      <div class="appointment-row">
        <span>Date:</span><span class="fill-line date"></span><span>at</span><span class="fill-line time"></span><span>AM</span><span class="check-box"></span><span>PM</span><span class="check-box"></span>
      </div>
    </div>
  </section>

</main>
</body>
</html>
```